Professional Business Card for Luxury Hotel & Resort Development Firm. Advisory firm

Project Overview: We are a specialized advisory firm focused on Hotel & Resort Development. Our clients are high-net-worth investors and major hospitality brands.

Design Requirements:

Style: Minimalist, sophisticated, and trustworthy. We want to avoid looking too "corporate" or "dry"—it should feel premium.

Key Elements: Please incorporate our logo [もしロゴがあれば] and emphasize a clean layout with plenty of white space.

Color Palette: We prefer Grey and White or Black and White to evoke a sense of luxury and stability.

Typography: Professional garamond, or sans-serif or elegant serif fonts

Goal: The card should feel substantial and high-end when handed to a client, reflecting our expertise in multi-million dollar developments.
Updates

I am currently on a business trip for field research and have limited access to my desktop. Additionally, I have just provided detailed technical feedback to a designer and am waiting for their refined proposals. To ensure the final logo meets the high standards of my new advisory firm, I would like to extend the deadline by 7 days. Thank you for your support.

Target Market(s)

High-net-worth investors, luxury hospitality brands, and real estate developers.

Contact Information for Business Card

Firm Name: Larkfield Counsel Partners, My Name: Kenji Morisawa, Title: Founder, Address 5-7-4 Kitakawabe Asahi Yokohama Japan 241-0815, email address: kmorisawa@larkfieldcp.com, Tel: +81 80-4821-3357. Front Site (Primary): Japanese translation of the back side, Please use a clean Japanese font (like Mincho) that complements the Garmond on the English side Back side: English. Note for Japanese text: since the frond side is the main fae, please ensure the layout is clean and professional. Please use a high-quality Mincho ( Serif-style) font for Japanese to mach the Garmond used on the English side. Text for Front side (Japanese) Larkfield Counsel Partners, 役職:代表、森沢健二、241-0815 横浜市旭区北川辺5-7-4. Name of the firm can stay in English.

Font styles to use
Other font styles liked:
• Font Preference: Please use Garamond for all text to maintain a consistent, elegant, and classic professional look.

Requirements
Must have
• Professional and clean layout, high-end feel.
Nice to have
• Minimalist design with subtle luxury accents.

```html
<!DOCTYPE html>
<html lang="en">
<head>
<meta charset="utf-8">
<title>Larkfield Counsel Partners – Business Card</title>
<link href="https://fonts.googleapis.com/css2?family=EB+Garamond:wght@400;500&family=Shippori+Mincho:wght@400;500&display=swap" rel="stylesheet">
<style>
  :root {
    --backdrop: #2b2c31;
    --card-white: #ffffff;
    --card-black: #1c1c1c;
    --ink: #1e1e1e;
    --ink-soft: #555555;
    --band: #3a3a3c;
    --band-text: #f2f2f2;
    --paper-text: #f5f5f5;
    --paper-soft: #c9c9c9;
  }
  html, body {
    margin: 0;
    padding: 0;
    width: 1200px;
    height: 900px;
    overflow: hidden;
    background: var(--backdrop);
    font-family: "EB Garamond", Garamond, serif;
  }
  .canvas {
    position: relative;
    width: 1200px;
    height: 900px;
  }
  .card {
    position: absolute;
    width: 560px;
    height: 320px;
    border-radius: 16px;
    overflow: hidden;
    box-sizing: border-box;
  }

  /* English side: contact details */
  .card-front {
    left: 80px;
    top: 100px;
    background: var(--card-white);
    color: var(--ink);
  }
  .front-brand {
    position: absolute;
    top: 38px;
    left: 0;
    right: 0;
    display: flex;
    flex-direction: column;
    align-items: center;
  }
  .front-brand .brand-name {
    font-size: 24px;
    letter-spacing: 0.06em;
    text-transform: uppercase;
    color: var(--ink);
    white-space: nowrap;
  }
  .front-brand .brand-rule {
    width: 300px;
    height: 1px;
    background: var(--ink);
    margin-top: 4px;
  }
  .front-person {
    position: absolute;
    top: 100px;
    left: 0;
    right: 0;
    text-align: center;
  }
  .person-name {
    font-size: 28px;
    letter-spacing: 0.05em;
    text-transform: uppercase;
    margin: 0;
    font-weight: 400;
    line-height: 1.2;
  }
  .person-title {
    font-size: 12px;
    letter-spacing: 0.32em;
    text-transform: uppercase;
    color: var(--ink-soft);
    margin: 2px 0 0;
  }
  .contact-list {
    list-style: none;
    margin: 14px 0 0;
    padding: 0;
    font-size: 18px;
  }
  .contact-list li {
    display: flex;
    align-items: center;
    justify-content: center;
    gap: 8px;
    line-height: 1.5;
  }
  .contact-list svg {
    width: 16px;
    height: 16px;
    fill: var(--ink);
  }
  .address-band {
    position: absolute;
    left: 0;
    bottom: 0;
    width: 560px;
    height: 58px;
  }
  .address-band svg.band-shape {
    position: absolute;
    inset: 0;
  }
  .address-text {
    position: absolute;
    left: 0;
    right: 0;
    bottom: 12px;
    display: flex;
    align-items: center;
    justify-content: center;
    gap: 8px;
    color: var(--band-text);
    font-size: 17px;
  }
  .address-text svg {
    width: 14px;
    height: 16px;
    fill: var(--band-text);
  }

  /* Japanese side: brand face */
  .card-back {
    left: 560px;
    top: 480px;
    padding: 0 40px;
    background: var(--card-black);
    color: var(--paper-text);
    display: flex;
    flex-direction: column;
    align-items: center;
    justify-content: center;
    text-align: center;
  }
  .back-brand {
    font-size: 30px;
    letter-spacing: 0.06em;
    text-transform: uppercase;
    color: var(--paper-text);
    white-space: nowrap;
  }
  .back-rule {
    width: 360px;
    height: 1px;
    background: var(--paper-text);
    margin: 6px 0 22px;
  }
  .jp-details {
    font-family: "Shippori Mincho", "Hiragino Mincho ProN", serif;
    color: var(--paper-text);
  }
  .jp-role-name {
    margin: 0;
    font-size: 20px;
    font-weight: 400;
    letter-spacing: 0.12em;
  }
  .jp-role {
    font-size: 13px;
    color: var(--paper-soft);
    margin-right: 14px;
    letter-spacing: 0.2em;
  }
  .jp-address {
    margin: 10px 0 0;
    font-size: 14px;
    letter-spacing: 0.08em;
    color: var(--paper-soft);
  }
</style>
</head>
<body>
<main class="canvas">
  <section class="card card-front" lang="en" aria-label="Business card, English side">
    <div class="front-brand">
      <div class="brand-name">Larkfield Counsel Partners</div>
      <div class="brand-rule"></div>
    </div>
    <div class="front-person">
      <h1 class="person-name">Kenji Morisawa</h1>
      <p class="person-title">Founder</p>
      <ul class="contact-list">
        <li>
          <svg viewBox="0 0 24 24" aria-hidden="true"><path d="M6.6 10.8c1.4 2.8 3.8 5.1 6.6 6.6l2.2-2.2c.3-.3.7-.4 1-.2 1.1.4 2.3.6 3.6.6.6 0 1 .4 1 1V20c0 .6-.4 1-1 1C10.6 21 3 13.4 3 4c0-.6.4-1 1-1h3.5c.6 0 1 .4 1 1 0 1.3.2 2.5.6 3.6.1.3 0 .7-.2 1z"/></svg>
          <span>+81 80-4821-3357</span>
        </li>
        <li>
          <svg viewBox="0 0 24 24" aria-hidden="true"><path d="M2 5h20v14H2z M4 7v.5l8 5.5 8-5.5V7z" fill-rule="evenodd"/></svg>
          <span>kmorisawa@larkfieldcp.com</span>
        </li>
      </ul>
    </div>
    <div class="address-band">
      <svg class="band-shape" width="560" height="58" viewBox="0 0 560 58" aria-hidden="true">
        <path d="M0 58 V30 H60 L80 12 Q84 8 90 8 H470 Q476 8 480 12 L500 30 H560 V58 Z" fill="var(--band)"/>
      </svg>
      <div class="address-text">
        <svg viewBox="0 0 24 28" aria-hidden="true"><path d="M12 0C5.9 0 1 4.9 1 11c0 8 11 17 11 17s11-9 11-17C23 4.9 18.1 0 12 0zm0 15a4 4 0 1 1 0-8 4 4 0 0 1 0 8z"/></svg>
        <span>5-7-4 Kitakawabe Asahi Yokohama Japan 241-0815</span>
      </div>
    </div>
  </section>

  <section class="card card-back" lang="ja" aria-label="Business card, Japanese side">
    <div class="back-brand" lang="en">Larkfield Counsel Partners</div>
    <div class="back-rule"></div>
    <div class="jp-details">
      <p class="jp-role-name"><span class="jp-role">代表</span>森沢健二</p>
      <p class="jp-address">〒241-0815 横浜市旭区北川辺5-7-4</p>
    </div>
  </section>
</main>
</body>
</html>
```